Golden Coat All-Purpose Breading Bag Design

Our client, Halvern Food Products, is looking to re-design the packaging for their product, Pellow's Golden Coat. Goldn Coat is an all-purpose food breading mix.

Halvern Foods has a registered trademark for this product, but they have not been using it for this particular 10 pound bag. They want to get the trademark onto the bag and also give the bag an updated look. They would like to continue to use the same red and blue colors. This 10 pound bag is not available on store shelves; it is sold to food service distributors who sell to restaurants.

All of the copy on the existing bag is still relevant, so we will want to incoprporate it into the bag design. Once these bags are filled with product, the tops get folded over about 1 inch and then sewn shut with thread.

Eventually, we will need the design applied to the Bag Template file attached, but that isn't important until a design is selected.

Target Market(s)

Restaurants

Industry/Entity Type

Food Manufacturing

Colors
0054AA
0677BA
7BADD7
CADEEF
E8F1F8
EB3D1F
EC4F4E
F09395
F8D3D4
FCEDEE

Requirements
Must have
• Trademark introduced to the design

```html
<!DOCTYPE html>
<html lang="en">
<head>
<meta charset="utf-8">
<title>Pellow's Golden Coat – 10 lb Bag Panels</title>
<link rel="stylesheet" href="https://fonts.googleapis.com/css2?family=Montserrat:wght@400;500;600;700;800&display=swap">
<style>
  :root{
    --bg:#e6e6e6;
    --paper:#f7f7f5;
    --red:#ec4f4e;
    --blue:#0054aa;
    --blue-mid:#0677ba;
    --ink:#2a2a2a;
    --white:#ffffff;
    --line:#3a3a3a;
  }
  *{box-sizing:border-box;margin:0;padding:0}
  html,body{width:1200px;height:900px;overflow:hidden;background:var(--bg)}
  body{font-family:"Montserrat",Arial,sans-serif;color:var(--ink);position:relative}

  .bag{position:absolute;top:130px;height:640px;display:flex;box-shadow:0 18px 30px rgba(0,0,0,.12)}
  .bag--breading{left:95px}
  .bag--frying{left:655px}
  .panel{position:relative;background:var(--paper);height:100%}
  .panel--front{width:300px;border-left:1px solid #d4d4d4;border-right:1px solid #d4d4d4}
  .panel--side{width:140px}

  .brand{position:absolute;left:0;right:0;text-align:center;color:var(--blue);font-weight:800;line-height:1.02}
  .panel--front .brand{top:80px;font-size:44px}
  .panel--front .brand__maker{display:block;font-size:22px;margin-bottom:10px}
  .panel--side .brand{top:150px;font-size:22px}
  .panel--side .brand__maker{display:block;font-size:12px;margin-bottom:6px}

  /* Left bag front */
  .claim{position:absolute;left:18px;right:18px;top:345px;height:82px;display:flex;gap:4px}
  .claim__main{flex:1 1 auto;background:var(--red);color:var(--white);text-align:center;padding:12px 4px 0}
  .claim__kicker{font-size:12px;font-weight:600;letter-spacing:.5px}
  .claim__title{font-size:27px;font-weight:800;letter-spacing:.5px;line-height:1.05}
  .claim__tag{font-size:7px;font-weight:600;letter-spacing:1px;margin-top:4px}
  .claim__side{width:72px;background:var(--red);color:var(--white);font-size:8.5px;font-weight:700;padding:8px 6px;line-height:1.35}
  .info{position:absolute;left:18px;right:18px;border:2px solid var(--line);background:var(--white);text-align:center}
  .info--ingredients{top:430px;height:110px}
  .info__head{font-size:11px;font-weight:700;letter-spacing:1.5px;color:var(--blue-mid);padding:8px 0 5px;border-bottom:2px solid var(--blue-mid);margin:0 18px}
  .info__body{font-size:10px;line-height:1.5;padding:9px 10px 0}
  .foot{position:absolute;left:18px;right:18px;top:540px;height:40px;background:var(--blue);color:var(--white);display:flex;align-items:center;justify-content:space-between;padding:0 8px;font-size:6.5px;line-height:1.4}
  .foot__note{width:95px;font-weight:600}
  .foot__company{width:90px}
  .foot__company strong{font-size:7.5px}
  .weight{position:absolute;left:50%;top:-14px;transform:translateX(-50%);width:56px;height:56px;border-radius:50%;background:var(--ink);color:var(--white);text-align:center;font-size:7px;padding-top:14px}
  .weight b{display:block;font-size:13px;font-weight:500}

  /* Left bag side */
  .story{position:absolute;left:12px;right:12px;top:300px;height:290px;background:var(--red);color:var(--white);border:2px solid var(--line);padding:12px 9px;font-size:8.2px;line-height:1.45;text-align:center}
  .story p+p{margin-top:10px}

  /* Right bag front */
  .use{position:absolute;left:18px;right:18px;top:345px;height:120px;background:var(--red);color:var(--white);text-align:center;padding-top:18px;border:2px solid var(--line);border-bottom:none}
  .use__small{font-size:13px;font-weight:600}
  .use__big{font-size:26px;font-weight:800;line-height:1.1}
  .use__note{font-size:8px;letter-spacing:.5px;margin-top:2px}
  .info--uses{top:465px;height:110px;border-top:none}

  /* Right bag side */
  .directions{position:absolute;left:12px;right:12px;top:300px;height:250px;border:2px solid var(--line);background:var(--white)}
  .directions__head{text-align:center;padding:10px 0 8px}
  .directions__kicker{font-size:8px;font-weight:700;letter-spacing:1px}
  .directions__title{font-size:14px;font-weight:800;letter-spacing:1.5px;color:var(--blue-mid)}
  .directions__steps{background:var(--red);color:var(--white);list-style:none;padding:10px 8px 12px;font-size:8.5px;line-height:1.4}
  .directions__steps li{padding-left:10px;position:relative;margin-bottom:6px}
  .directions__steps li::before{content:"";position:absolute;left:0;top:4px;width:4px;height:4px;border-radius:50%;background:var(--white)}
  .directions__tip{font-size:8px;padding:10px 8px;line-height:1.4}
</style>
</head>
<body>

<section class="bag bag--breading">
  <div class="panel panel--side">
    <div class="brand"><span class="brand__maker">Pellow's</span>Golden Coat</div>
    <div class="story">
      <p>Pellow's Golden Coat is a prepared formula of pure foods that enables you to fry chicken from the raw to the well done in ten minutes. It seals in all the natural juice and creates a very thin crunchy coating which the fat does not penetrate, thereby using much less fat than ordinary frying methods.</p>
      <p>This formula is an all-dry mix to be used on anything breaded: fish, oysters, shrimp, veal and chicken fried steak.</p>
    </div>
  </div>
  <div class="panel panel--front">
    <div class="brand"><span class="brand__maker">Pellow's</span>Golden<br>Coat</div>
    <div class="claim">
      <div class="claim__main">
        <div class="claim__kicker">THE ALL PURPOSE</div>
        <div class="claim__title">BREADING</div>
        <div class="claim__tag">SEALS JUICE IN · GREASE OUT</div>
      </div>
      <div class="claim__side">FOOD FRIED THE GOLDEN COAT WAY IS FRIED FOOD THE RIGHT WAY</div>
    </div>
    <div class="info info--ingredients">
      <div class="info__head">INGREDIENTS</div>
      <p class="info__body">flour, salt, non fat milk solids, egg yolk, baking powder, corn starch, sugar and pepper</p>
    </div>
    <div class="foot">
      <span class="foot__note">Cooks two-pound chicken well done in 10 minutes deep fat</span>
      <span class="weight">Net Wt<b>10 Lbs</b></span>
      <span class="foot__company"><strong>Halvern Food Products</strong><br>418 Harlow Road<br>Cedar Falls, Iowa 50613</span>
    </div>
  </div>
</section>

<section class="bag bag--frying">
  <div class="panel panel--front">
    <div class="brand"><span class="brand__maker">Pellow's</span>Golden<br>Coat</div>
    <div class="use">
      <div class="use__small">FOR</div>
      <div class="use__big">DEEP FAT</div>
      <div class="use__small">AND</div>
      <div class="use__big">PAN FRYING</div>
      <div class="use__note">(slightly longer on pan frying)</div>
    </div>
    <div class="info info--uses">
      <div class="info__head">CAN BE USED FOR</div>
      <p class="info__body">chicken, steaks, chops, tenderloin, fish, shrimp, oyster and other sea foods, onion rings and vegetables</p>
    </div>
  </div>
  <div class="panel panel--side">
    <div class="brand"><span class="brand__maker">Pellow's</span>Golden Coat</div>
    <div class="directions">
      <div class="directions__head">
        <div class="directions__kicker">NOTHING TO ADD</div>
        <div class="directions__title">DIRECTIONS</div>
      </div>
      <ul class="directions__steps">
        <li>Wet all foods in water</li>
        <li>Place in dry dip, coating thoroughly</li>
        <li>Deep fry at 350°F for 10 minutes</li>
      </ul>
      <p class="directions__tip">For best results double dip onion rings and oysters</p>
    </div>
  </div>
</section>

</body>
</html>
```